Wexley Foot & Ankle Ashbrook Window Vinyl Cling

Hi,
I'm looking to get a window decal done, but need it professionally designed.
-must be 24" x 24"
-Quorum Font
-Include our logo, Podiatry, phone number and website
- The goal is to make this eye catching.
Thank you,
Dorian

```html
<!DOCTYPE html>
<html lang="en">
<head>
<meta charset="utf-8">
<title>Wexley Foot &amp; Ankle Ashbrook – Window Cling</title>
<link rel="stylesheet" href="https://fonts.googleapis.com/css2?family=Poppins:wght@400;600;700;800&display=swap">
<style>
  :root {
    --paper: #f4f5f7;
    --sheen: #fbfbfc;
    --shade: #e9eaec;
    --frame: #bfc0c4;
    --orange: #f47f48;
    --teal: #52c8ac;
    --ink: #35363a;
    --white: #ffffff;
  }
  html, body {
    margin: 0;
    padding: 0;
    width: 1200px;
    height: 1200px;
    overflow: hidden;
    background: var(--paper);
  }
  .cling {
    display: block;
    width: 1200px;
    height: 1200px;
    font-family: "Poppins", sans-serif;
  }
  .cling__paper { fill: var(--paper); }
  .cling__sheen { fill: var(--sheen); }
  .cling__shade { fill: var(--shade); opacity: .7; }
  .cling__frame { fill: none; stroke: var(--frame); stroke-width: 3; }
  .brand__dot { fill: var(--teal); }
  .brand__name { fill: var(--orange); font-weight: 700; }
  .headline { fill: var(--orange); font-weight: 800; }
  .specialty { fill: var(--ink); font-weight: 600; }
  .call-band { fill: var(--teal); }
  .call-icon__ring { fill: var(--ink); stroke: var(--teal); stroke-width: 4; }
  .call-icon__handset { fill: var(--white); }
  .call-icon__waves { fill: none; stroke: var(--white); stroke-width: 3.5; stroke-linecap: round; }
  .call-number { fill: var(--ink); font-weight: 700; }
  .website { fill: var(--ink); font-weight: 400; }
  .website__name { fill: var(--orange); font-weight: 700; }
</style>
</head>
<body>
<svg class="cling" viewBox="0 0 1200 1200" xmlns="http://www.w3.org/2000/svg" role="img" aria-label="Wexley Foot and Ankle Ashbrook podiatry window cling">
  <!-- background with diagonal light streaks -->
  <rect class="cling__paper" x="0" y="0" width="1200" height="1200"/>
  <polygon class="cling__sheen" points="1120,0 1200,0 1200,40 100,1200 0,1200 0,1180"/>
  <polygon class="cling__shade" points="1200,40 1200,300 0,1080 0,990"/>
  <polygon class="cling__sheen" points="1200,300 1200,370 180,1200 120,1200"/>
  <polygon class="cling__shade" points="1200,470 1200,560 0,1200 0,1120"/>

  <!-- frame with opening for the brand -->
  <path class="cling__frame" d="M175,168 H114 A47,47 0 0 0 67,215 V967 A47,47 0 0 0 114,1014 H1084 A47,47 0 0 0 1131,967 V215 A47,47 0 0 0 1084,168 H1035"/>

  <!-- brand -->
  <g class="brand">
    <circle class="brand__dot" cx="335" cy="185" r="72"/>
    <text class="brand__name" x="978" y="160" font-size="80" text-anchor="end">WEXLEY</text>
    <text class="brand__name" x="978" y="232" font-size="78" text-anchor="end">FOOT &amp; ANKLE</text>
    <text class="brand__name" x="978" y="282" font-size="48" text-anchor="end">ASHBROOK</text>
  </g>

  <!-- headline -->
  <text class="headline" x="606" y="536" font-size="206" text-anchor="middle" textLength="965" lengthAdjust="spacingAndGlyphs">PODIATRY</text>
  <text class="specialty" x="599" y="663" font-size="108" text-anchor="middle" textLength="738" lengthAdjust="spacingAndGlyphs">FOOT &amp; ANKLE</text>
  <text class="specialty" x="599" y="779" font-size="106" text-anchor="middle" textLength="617" lengthAdjust="spacingAndGlyphs">PHYSICIANS</text>

  <!-- call band -->
  <path class="call-band" d="M68,875 H1130 V967 A46,46 0 0 1 1084,1013 H114 A46,46 0 0 1 68,967 Z"/>
  <g class="call-icon" transform="translate(137 942)">
    <circle class="call-icon__ring" r="42"/>
    <path class="call-icon__handset" transform="translate(-18 -16) scale(1.5)" d="M6.6,10.8c1.4,2.8,3.8,5.1,6.6,6.6l2.2-2.2c0.3-0.3,0.7-0.4,1-0.2c1.1,0.4,2.3,0.6,3.6,0.6c0.6,0,1,0.4,1,1V20c0,0.6-0.4,1-1,1C10.6,21,3,13.4,3,4c0-0.6,0.4-1,1-1h3.5c0.6,0,1,0.4,1,1c0,1.3,0.2,2.5,0.6,3.6c0.1,0.3,0,0.7-0.2,1L6.6,10.8z"/>
    <path class="call-icon__waves" d="M4,-14 A12,12 0 0 1 16,-2"/>
    <path class="call-icon__waves" d="M5,-24 A22,22 0 0 1 26,-3"/>
  </g>
  <text class="call-number" x="204" y="977" font-size="104" textLength="900" lengthAdjust="spacingAndGlyphs">Call (877) 555-0148</text>

  <!-- website -->
  <text class="website" x="598" y="1118" font-size="86" text-anchor="middle" textLength="836" lengthAdjust="spacingAndGlyphs">www.<tspan class="website__name">StepWellFeet</tspan>.com</text>
</svg>
</body>
</html>
```